Football tournament flyer

I would like a quick turn around for this please.
I need a flyer to promote an 11 aside football tournament I am organising to celebrate the 23rd independence of my country Somaliland. Please use the national colours of our flag in the flyer, I have attached a file for your consideration.
The tournament will take place on 10/05/2014, from 9am - 8pm. The venue will be Corrin Open Space, Tavistrel Lane, Enfield, EN7 2QR.
Refreshments, food and entertainment will be provided.
The name of the cup is Warsadle Cup.
Spaces are limited and the entry fee per team is £200. All proceeds are for charity projects in Somaliland.
To register a team contact Faisal Warsame on 07521 804 192 or Bashir Yusuf on 07463 125 870.
The best players will have the opportunity to represent Somaliland in an international game on the 17/05/2014.
The tournament is organised by Dalmar FC and EverKindred Foundation.

```html
<!DOCTYPE html>
<html lang="en">
<head>
<meta charset="utf-8">
<title>Warsadle Cup – Football Tournament Flyer</title>
<link rel="stylesheet" href="https://fonts.googleapis.com/css2?family=Bebas+Neue&family=Anton&display=swap">
<style>
  :root {
    --page-bg: #e6e6e6;
    --flag-green: #1c9a46;
    --flag-blue: #2a6fd6;
    --flag-red: #d9221e;
    --grass-light: #58b13a;
    --grass-dark: #2f7d1e;
    --red-box: #c8141a;
    --red-box-dark: #8f0b10;
    --ink: #141414;
    --white: #ffffff;
    --yellow: #ffe11a;
  }
  * { margin: 0; padding: 0; box-sizing: border-box; }
  html, body { width: 996px; height: 1200px; overflow: hidden; background: var(--page-bg); }
  body { font-family: "Bebas Neue", "Oswald", sans-serif; position: relative; }

  .flyer {
    position: absolute; left: 110px; top: 98px; width: 776px; height: 1005px;
    overflow: hidden;
    background: linear-gradient(180deg, var(--grass-light) 0%, var(--grass-dark) 100%);
  }
  .flyer > * { position: absolute; white-space: nowrap; }

  .sky-art {
    left: 0; top: 0; width: 776px; height: 330px;
    background:
      linear-gradient(180deg, rgba(255,255,255,0) 55%, var(--grass-light) 100%),
      linear-gradient(90deg, var(--flag-green) 0%, #4fb5c9 38%, var(--flag-blue) 55%, #b83b5a 75%, var(--flag-red) 100%);
  }
  .stadium-art {
    left: 0; top: 260px; width: 776px; height: 140px;
    background: linear-gradient(180deg, rgba(60,70,60,0.55) 0%, rgba(70,140,50,0) 100%);
  }
  .balls-art {
    left: 120px; top: 225px; width: 550px; height: 240px;
    background: radial-gradient(ellipse at 50% 55%, rgba(245,245,245,0.95) 0%, rgba(200,200,200,0.85) 45%, rgba(200,200,200,0) 72%);
  }

  .title {
    left: 0; width: 776px; top: 357px; text-align: center;
    font-family: "Anton", sans-serif; font-size: 116px; line-height: 1;
    color: var(--white);
    text-shadow: 0 2px 0 #bdbdbd, 0 4px 0 #8a8a8a, 0 8px 14px rgba(0,0,0,0.55);
  }
  .organisers {
    left: 0; width: 776px; top: 512px; text-align: center;
    font-size: 21px; color: var(--ink); letter-spacing: 1.2px;
  }

  .date {
    left: 48px; top: 550px; font-size: 78px; line-height: 1; letter-spacing: -1px; color: var(--white);
    text-shadow: 0 3px 6px rgba(0,0,0,0.45);
  }
  .divider { left: 425px; top: 556px; width: 2px; height: 66px; background: var(--white); }
  .venue { left: 438px; top: 554px; color: var(--white); line-height: 1; text-shadow: 0 2px 4px rgba(0,0,0,0.4); }
  .venue-name { display: block; font-size: 42px; }
  .venue-address { display: block; font-size: 26px; margin-top: 4px; }

  .clock { left: 52px; top: 643px; width: 54px; height: 54px; }
  .time {
    left: 122px; top: 636px; font-size: 64px; line-height: 1; color: var(--white);
    text-shadow: 0 3px 6px rgba(0,0,0,0.45);
  }
  .entry-note {
    left: 50px; top: 712px; font-size: 35px; line-height: 36px; color: var(--white);
    text-shadow: 0 2px 5px rgba(0,0,0,0.45);
  }
  .chevron { left: 362px; top: 728px; width: 28px; height: 34px; }

  .fee-box {
    left: 405px; top: 642px; width: 343px; height: 152px; border-radius: 10px;
    background: linear-gradient(180deg, var(--red-box-dark) 0%, var(--red-box) 22%, var(--red-box) 80%, var(--red-box-dark) 100%);
    box-shadow: 0 6px 12px rgba(0,0,0,0.4);
  }
  .fee-amount {
    left: 414px; top: 656px; font-size: 120px; line-height: 1; color: var(--white);
    text-shadow: 0 3px 5px rgba(0,0,0,0.4);
  }
  .fee-note { left: 604px; top: 666px; width: 140px; text-align: center; color: var(--white); line-height: 1; }
  .fee-note .small { display: block; font-size: 18px; margin-bottom: 4px; }
  .fee-note .large { display: block; font-size: 28px; line-height: 27px; }

  .kicker-art {
    left: 45px; top: 805px; width: 195px; height: 100px;
    background: radial-gradient(ellipse at 50% 55%, rgba(10,20,10,0.8) 0%, rgba(10,20,10,0.35) 45%, rgba(10,20,10,0) 72%);
  }
  .details { right: 54px; top: 804px; text-align: right; color: var(--white); line-height: 1; text-shadow: 0 2px 4px rgba(0,0,0,0.4); }
  .details .perks { display: block; font-size: 25px; }
  .details .highlight { display: block; font-size: 33px; margin-top: 7px; }
  .details .fine { display: block; font-size: 20px; margin-top: 6px; }

  .register-tab {
    left: 232px; top: 918px; width: 310px; height: 30px;
    background: var(--red-box); border-radius: 8px 8px 0 0;
    color: var(--yellow); font-size: 28px; line-height: 32px; text-align: center;
  }
  .contact-band {
    left: 0; top: 946px; width: 776px; height: 59px;
    background: linear-gradient(180deg, var(--flag-red) 0%, var(--red-box-dark) 100%);
    color: var(--white); font-size: 34px; line-height: 60px; text-align: center;
  }
  .contact-band .name { color: var(--ink); }
</style>
</head>
<body>
  <main class="flyer">
    <div class="sky-art" role="img" aria-label="Cloudy sky in green, blue and red flag colours with silhouetted footballers"></div>
    <div class="stadium-art" role="img" aria-label="Stadium stands behind a grass pitch"></div>
    <div class="balls-art" role="img" aria-label="Three footballs resting on the pitch"></div>

    <h1 class="title">WARSADLE CUP</h1>
    <p class="organisers">ORGANISED BY DALMAR FC AND EVERKINDRED FOUNDATION</p>

    <p class="date">10TH MAY 2014</p>
    <div class="divider"></div>
    <p class="venue">
      <span class="venue-name">CORRIN OPEN SPACE,</span>
      <span class="venue-address">TAVISTREL LANE, ENFIELD, EN7 2QR</span>
    </p>

    <svg class="clock" viewBox="0 0 54 54" aria-hidden="true">
      <circle cx="27" cy="27" r="22" fill="none" stroke="#d9221e" stroke-width="6"/>
      <path d="M27 14 V28 H38" fill="none" stroke="#d9221e" stroke-width="5" stroke-linecap="round"/>
    </svg>
    <p class="time">9AM - 8PM</p>
    <p class="entry-note">SPACES ARE LIMITED AND THE<br>ENTRY FEE PER TEAM IS</p>
    <svg class="chevron" viewBox="0 0 28 34" aria-hidden="true">
      <path d="M4 3 L22 17 L4 31" fill="none" stroke="#ffffff" stroke-width="7"/>
    </svg>

    <div class="fee-box"></div>
    <p class="fee-amount">£200</p>
    <p class="fee-note">
      <span class="small">ALL PROCEEDS ARE</span>
      <span class="large">FOR CHARITY<br>PROJECTS IN<br>SOMALILAND</span>
    </p>

    <div class="kicker-art" role="img" aria-label="Silhouette of a player making an overhead kick"></div>
    <p class="details">
      <span class="perks">REFRESHMENTS, FOOD AND ENTERTAINMENT WILL BE PROVIDED</span>
      <span class="highlight">THE BEST PLAYERS WILL HAVE THE OPPORTUNITY</span>
      <span class="fine">TO REPRESENT SOMALILAND IN AN INTERNATIONAL GAME ON THE 17/05/2014.</span>
    </p>

    <div class="register-tab">TO REGISTER A TEAM CONTACT</div>
    <p class="contact-band"><span class="name">FAISAL WARSAME</span> - 07521 804 192 OR <span class="name">BASHIR YUSUF</span> - 07463 125 870</p>
  </main>
</body>
</html>
```